Long Established Local Fencing (not swords) Business needs fresh Business Cards

We need fresh double sided business cards for our Fencing Construction business, we are looking for something with our new logo design added, and maybe a photo background ?
We recently had cards made from Quillmarko and we were horrified with what we got back, the quality was terrible, so am looking for high quality format for good printing company to make.
We install Steelwave, Timber paling, Aluminium Slat Screening, Picket (timber and aluminium) and most other fencing installations.
Our website is brelbanfencing.com.au should you like to learn a bit more.
We do have logo in other formats if required.
We have been in business for over 35 years and we have used this as a "motto" it is on our signage

Industry/Entity Type

Construction

Contact Information for Business Card

Open to ideas, we need 3 x different cards, one generic with no name and 2 x others each with 1 of our bosses name on each, I will put into upload files.

Colors
ec1f27
000000
606060
f5f5f5

Requirements
Must have
• Company Name and Logo
• Address
• Contact details, phone, website, email etc
• Small space to write notes when leaving card at residence
Nice to have
• Our motto "Servicing the Peninsula for over 35 years"

```html
<!DOCTYPE html>
<html lang="en">
<head>
<meta charset="utf-8">
<title>Business Card Generic</title>
<link href="https://fonts.googleapis.com/css2?family=Archivo+Black&family=Bebas+Neue&family=Oswald:wght@500&family=Arimo:wght@400&display=swap" rel="stylesheet">
<style>
  :root {
    --red: #c8262a;
    --black: #1c1b1c;
    --ink: #141414;
    --grey: #606060;
    --card: #e9e9e9;
    --light: #f5f5f5;
  }
  * { margin: 0; padding: 0; box-sizing: border-box; }
  html, body { width: 1200px; height: 965px; overflow: hidden; }
  body {
    background: linear-gradient(#cfcfcf, #e6e6e6);
    font-family: 'Arimo', Arial, sans-serif;
    position: relative;
  }
  .board-title {
    position: absolute; top: 40px; left: 0; width: 1200px;
    text-align: center;
    font-family: 'Bebas Neue', 'Oswald', sans-serif;
    font-size: 104px; line-height: 1; color: var(--black);
    letter-spacing: 0.5px;
  }
  .card {
    position: absolute; left: 304px; width: 590px; height: 336px;
    background: var(--card);
    box-shadow: 0 3px 5px rgba(0,0,0,0.35);
    overflow: hidden;
  }
  .card-front { top: 198px; }
  .card-back { top: 569px; height: 337px; }

  .company-name {
    font-family: 'Archivo Black', sans-serif;
    color: var(--black); text-transform: uppercase; line-height: 1;
  }
  .card-front .company-name {
    position: absolute; left: 29px; top: 24px; font-size: 44px; letter-spacing: 1px;
  }
  .company-name span { display: block; }
  .company-name span + span { margin-top: 4px; }

  .motto {
    position: absolute; right: 28px; top: 22px; text-align: right;
    font-family: 'Oswald', sans-serif; font-weight: 500;
    font-size: 20px; line-height: 28px; color: var(--black);
    text-transform: uppercase; transform: scaleX(0.85); transform-origin: right;
  }
  .motto .accent { color: var(--red); }

  .contact-band {
    position: absolute; left: 0; top: 137px; width: 516px; height: 133px;
    background: var(--black); color: #eee;
  }
  .accent-block {
    position: absolute; left: 516px; top: 137px; width: 74px; height: 133px;
    background: var(--red);
  }
  .address {
    position: absolute; left: 29px; top: 12px; font-size: 16px; line-height: 20px;
  }
  .contact-list { position: absolute; left: 29px; top: 62px; list-style: none; }
  .contact-list li {
    display: flex; align-items: center; gap: 10px;
    font-size: 16px; line-height: 20px;
  }
  .contact-list svg { width: 14px; height: 14px; flex: none; }

  .card-back .brand-block {
    position: absolute; left: 0; top: 40px; width: 590px; text-align: center;
  }
  .card-back .company-name { font-size: 44px; letter-spacing: 1px; }
  .licence {
    margin-top: 14px; font-size: 17px; letter-spacing: 5px; color: var(--black);
  }
  .licence .label { color: var(--red); }

  .note-line {
    position: absolute; left: 18px; width: 554px; height: 1px; background: var(--black);
  }
  .note-line.one { top: 191px; }
  .note-line.two { top: 225px; }
  .note-line.three { top: 258px; }

  .footer-rule {
    position: absolute; left: 0; top: 288px; width: 590px; height: 3px; background: var(--red);
  }
  .footer-band {
    position: absolute; left: 0; top: 292px; width: 590px; height: 45px;
    background: var(--ink); color: #eee;
    display: flex; align-items: center; justify-content: center;
    font-size: 16px; letter-spacing: 3px;
  }
  .footer-band .label { color: var(--red); margin-right: 8px; }
</style>
</head>
<body>
  <h1 class="board-title">Business Card Generic</h1>

  <section class="card card-front">
    <div class="company-name"><span>Brelban</span><span>Fencing</span></div>
    <p class="motto">Proudly servicing<br>the peninsula for<br><span class="accent">over 35 years</span></p>

    <div class="contact-band">
      <p class="address">42 KEEL ST, BRELBAN,<br>NSW, 2260</p>
      <ul class="contact-list">
        <li>
          <svg viewBox="0 0 14 14"><circle cx="7" cy="7" r="7" fill="#c8262a"/><path d="M4.5 3.5l1.6 1.8-.8 1c.5 1 1.2 1.7 2.2 2.2l1-.8 1.8 1.6-.9 1.2C6.6 10.3 3.7 7.4 3.5 4.4z" fill="#1c1b1c"/></svg>
          (02) 43880157
        </li>
        <li>
          <svg viewBox="0 0 14 14"><circle cx="7" cy="7" r="7" fill="#c8262a"/><rect x="3.5" y="4.5" width="7" height="5" fill="none" stroke="#1c1b1c" stroke-width="1"/><path d="M3.5 4.5L7 7.5l3.5-3" fill="none" stroke="#1c1b1c" stroke-width="1"/></svg>
          brelbanfencing@mailcove.com
        </li>
        <li>
          <svg viewBox="0 0 14 14"><circle cx="7" cy="7" r="7" fill="#c8262a"/><circle cx="7" cy="7" r="3.8" fill="none" stroke="#1c1b1c" stroke-width="0.9"/><path d="M3.2 7h7.6M7 3.2v7.6" stroke="#1c1b1c" stroke-width="0.9"/></svg>
          www.brelbanfencing.com.au
        </li>
      </ul>
    </div>
    <div class="accent-block"></div>
  </section>

  <section class="card card-back">
    <div class="brand-block">
      <div class="company-name"><span>Brelban</span><span>Fencing</span></div>
      <p class="licence"><span class="label">License No.</span> 51724c</p>
    </div>
    <div class="note-line one"></div>
    <div class="note-line two"></div>
    <div class="note-line three"></div>
    <div class="footer-rule"></div>
    <div class="footer-band"><span class="label">ABN</span>31208774651</div>
  </section>
</body>
</html>
```